Bref créative
The Halvorn Group, P.C. Biz Cards, letterhead, envelop, thank you cards, and powerpoint template
Biz Cards, letterhead, envelop, thank you cards, and powerpoint template
Professional
The Halvorn Group, P.C.
Dale Morvant
512 E. Tansy Avenue #407
Lawrenceville, GA 30719
Dale@ClearPathDWI.com
www.ClearPathDWI.com
I would like two different, but similar designs. One that incorporates the ClearPathDWI.com prominently, and one that doesn't have it at all. The design that doesn't incorporate clearpathdwi.com the email address is Dale@HalvornGroup.com. I tried to upload my logo, but I can't figure out where to do it. I'll get help tomorrow.

```html
<!DOCTYPE html>
<html lang="en">
<head>
<meta charset="utf-8">
<title>The Halvorn Group, P.C. — Business Cards</title>
<link rel="stylesheet" href="https://fonts.googleapis.com/css2?family=Marcellus&family=Open+Sans:wght@400;600;700&display=swap">
<style>
  :root {
    --backdrop: #ebe6de;
    --card: #ffffff;
    --card-edge: #d8d3cb;
    --ink: #3a3f4a;
    --brand-navy: #2f3d5e;
    --brand-blue: #2c6aa6;
    --rule-navy: #223a6b;
    --grey-light: #c9cacc;
    --grey-dark: #8f9194;
    --white: #ffffff;
  }
  * { box-sizing: border-box; margin: 0; padding: 0; }
  html, body { width: 1200px; height: 758px; overflow: hidden; }
  body { background: var(--backdrop); font-family: "Open Sans", Arial, sans-serif; color: var(--ink); position: relative; }

  .card {
    position: absolute;
    width: 514px;
    height: 297px;
    background: var(--card);
    border: 1px solid var(--card-edge);
    box-shadow: 0 2px 6px rgba(0,0,0,0.12);
    overflow: hidden;
  }
  .card--front-contact { left: 55px; top: 53px; }
  .card--front-brand { left: 620px; top: 53px; width: 520px; }
  .card--back-grey {
    left: 365px; top: 403px;
    background: radial-gradient(ellipse at 50% 45%, #d2d3d5 0%, var(--grey-light) 40%, var(--grey-dark) 100%);
    border-color: #9a9c9f;
  }

  .brand { position: absolute; display: flex; align-items: center; gap: 12px; }
  .brand__mark { width: 48px; height: 48px; border-radius: 50%; background: var(--brand-blue); flex: none; }
  .brand__name { font-family: "Marcellus", Georgia, serif; color: var(--brand-navy); line-height: 1; }
  .brand__primary { display: block; font-size: 30px; }
  .brand__secondary { display: block; font-size: 19px; margin-top: 6px; letter-spacing: 0.5px; }
  .card--front-contact .brand { left: 58px; top: 38px; }
  .card--front-brand .brand { left: 50%; top: 92px; transform: translateX(-50%); }
  .brand--large .brand__mark { width: 58px; height: 58px; }
  .brand--large .brand__primary { font-size: 34px; }
  .brand--large .brand__secondary { font-size: 21px; }
  .card--back-grey .brand { left: 50%; top: 88px; transform: translateX(-50%); }
  .card--back-grey .brand__mark { background: var(--white); }
  .card--back-grey .brand__name { color: var(--white); }

  .contact { position: absolute; left: 0; right: 0; top: 176px; text-align: center; font-size: 11px; line-height: 17px; color: var(--ink); }
  .contact__row { display: flex; justify-content: center; align-items: center; gap: 6px; }
  .icon { width: 9px; height: 9px; fill: var(--brand-navy); }

  .rule { position: absolute; left: 0; right: 0; top: 248px; height: 2px; background: var(--rule-navy); }
  .rule__accent { position: absolute; left: 0; top: -2px; width: 52px; height: 5px; background: var(--brand-blue); }

  .signature { position: absolute; left: 0; right: 0; top: 266px; text-align: center; font-size: 13px; color: var(--ink); }
  .signature__firm { font-weight: 700; }
  .signature__divider { color: var(--brand-blue); margin: 0 6px; }
  .signature__person { font-size: 11.5px; }

  .website { position: absolute; left: 0; right: 0; text-align: center; font-size: 11px; letter-spacing: 0.3px; }
  .card--front-brand .website { top: 256px; color: var(--ink); }
  .card--back-grey .website { top: 251px; color: var(--white); font-weight: 600; }
</style>
</head>
<body>

  <section class="card card--front-contact" aria-label="Business card front with contact details">
    <div class="brand">
      <span class="brand__mark"></span>
      <span class="brand__name">
        <span class="brand__primary">ClearPathDWI</span>
        <span class="brand__secondary">THE HALVORN GROUP, P.C.</span>
      </span>
    </div>
    <div class="contact">
      <div class="contact__row">512 E. Tansy Avenue #407 Lawrenceville, GA 30719</div>
      <div class="contact__row">
        <svg class="icon" viewBox="0 0 10 10"><path d="M2 0h2l1 2.5-1.3 1a6 6 0 0 0 2.8 2.8l1-1.3L10 6v2a2 2 0 0 1-2 2A8 8 0 0 1 0 2a2 2 0 0 1 2-2z"/></svg>
        <span>404-555-0182</span>
        <svg class="icon" viewBox="0 0 10 10"><rect x="0" y="3" width="10" height="6" rx="1"/><rect x="2" y="0" width="6" height="3"/></svg>
        <span>404-555-0187</span>
      </div>
      <div class="contact__row">
        <svg class="icon" viewBox="0 0 10 10"><path d="M0 2h10v6H0z M0 2l5 3.5L10 2" /></svg>
        <span>Dale@ClearPathDWI.com</span>
        <svg class="icon" viewBox="0 0 10 10"><circle cx="5" cy="5" r="5"/></svg>
        <span>www.ClearPathDWI.com</span>
      </div>
    </div>
    <div class="rule"><span class="rule__accent"></span></div>
    <p class="signature">
      <span class="signature__firm">The Halvorn Group, P.C.</span><span class="signature__divider">/</span><span class="signature__person">Dale Morvant</span>
    </p>
  </section>

  <section class="card card--front-brand" aria-label="Business card brand side">
    <div class="brand brand--large">
      <span class="brand__mark"></span>
      <span class="brand__name">
        <span class="brand__primary">ClearPathDWI</span>
        <span class="brand__secondary">THE HALVORN GROUP, P.C.</span>
      </span>
    </div>
    <p class="website">www.ClearPathDWI.com</p>
  </section>

  <section class="card card--back-grey" aria-label="Business card grey reverse">
    <div class="brand brand--large">
      <span class="brand__mark"></span>
      <span class="brand__name">
        <span class="brand__primary">ClearPathDWI</span>
        <span class="brand__secondary">THE HALVORN GROUP, P.C.</span>
      </span>
    </div>
    <p class="website">www.ClearPathDWI.com</p>
  </section>

</body>
</html>
```